Postcard Design

I need a postcard/flyer designed to advertise my nail business. I am qualified with Palm and Polish Academy UK and insured with QERVOL. I am offering Lustrea nail

I am fully mobile with flexible appointments. Beautiful nails for up to 3 weeks. No chipping, dulling or fading.

Prices: Fingernails £20. Toenails £20. Both for £35. Gel removal £10

Call Moira on 07812604731 or email lustrea_nails@brivomail.com can also follow on Chirper @Lustrea_nails.

Was hoping for a colourful and classy design, maybe a bit vintage that will appeal to all ages. Especially for weddings/honeymoons. Doesnt necessarily have to feature pictures of manicures/pedicures/hands/feet etc.

hope this all makes sense!

Moira

Industry/Entity Type

Business

Font styles to use
Serif

Colors
e567a6
34b8a4
33a6d7
b768aa
86cfc6
f04a50
d3a5cc

```html
<!DOCTYPE html>
<html lang="en">
<head>
<meta charset="utf-8">
<title>Lustrea Nail – Postcard</title>
<link rel="stylesheet" href="https://fonts.googleapis.com/css2?family=Elsie:wght@400;900&display=swap">
<style>
  :root {
    --paper-light: #ecd0a8;
    --paper-mid: #e2bd91;
    --paper-dark: #d4a97c;
    --title: #9b1b45;
    --ink: #3a1f2e;
    --contact: #6b2a5e;
    --accent-pink: #e567a6;
    --stroke-purple: #b768aa;
    --stroke-blue: #33a6d7;
    --stroke-yellow: #d8d66a;
    --stroke-coral: #f07a5a;
    --ticket: #e8a3c0;
  }
  * { margin: 0; padding: 0; box-sizing: border-box; }
  html, body { width: 1200px; height: 924px; overflow: hidden; background: var(--paper-mid); }
  .postcard {
    position: relative;
    width: 1200px;
    height: 924px;
    overflow: hidden;
    background:
      radial-gradient(ellipse at 30% 35%, rgba(255,240,215,0.55), transparent 60%),
      radial-gradient(ellipse at 80% 85%, rgba(190,140,95,0.25), transparent 55%),
      linear-gradient(160deg, var(--paper-light), var(--paper-mid) 55%, var(--paper-dark));
    font-family: "Elsie", serif;
    font-weight: 400;
  }
  .art { position: absolute; }
  .art--hand-rose {
    left: 500px; top: 42px; width: 280px; height: 150px;
    border-radius: 40% 45% 40% 50%;
    background: radial-gradient(ellipse at 45% 55%, #c98a5e, #d9a078 60%, rgba(226,189,145,0) 100%);
  }
  .art--portrait {
    left: 955px; top: 25px; width: 208px; height: 325px;
    background: linear-gradient(170deg, #a58a6c, #c6ad8c 55%, #b59878);
  }
  .art--ticket {
    left: 1005px; top: 305px; width: 190px; height: 95px;
    transform: rotate(-12deg);
    background: var(--ticket);
    opacity: 0.85;
  }
  .art--boot-bouquet {
    left: 265px; top: 565px; width: 175px; height: 325px;
    border-radius: 45% 45% 20% 20%;
    background: linear-gradient(180deg, #c99a52 0%, #b88a4c 30%, #7fb8b4 55%, #8cc4c0 100%);
  }
  .art--scene {
    left: 28px; top: 682px; width: 272px; height: 212px;
    background: linear-gradient(160deg, #bfa98a, #a99273 60%, #c2ae90);
  }
  .brand {
    position: absolute; left: 118px; top: 78px;
    font-weight: 900;
    font-size: 62px; color: var(--title); letter-spacing: 1px;
    white-space: nowrap;
  }
  .tagline {
    position: absolute; left: 175px; top: 204px;
    font-size: 34px; line-height: 46px; color: var(--ink);
    font-weight: 900; letter-spacing: 0.5px; white-space: nowrap;
  }
  .contact {
    position: absolute; left: 175px; top: 372px;
    font-size: 34px; line-height: 50px; color: var(--contact);
    font-weight: 900; letter-spacing: 0.5px; white-space: nowrap;
  }
  .strokes { position: absolute; left: 620px; top: 586px; width: 560px; height: 140px; }
  .prices {
    position: absolute; left: 615px; top: 548px;
    font-size: 34px; line-height: 45px; color: var(--ink);
    font-weight: 900; letter-spacing: 0.5px;
  }
  .prices__row { display: flex; width: 330px; justify-content: space-between; white-space: nowrap; }
  .credentials {
    position: absolute; left: 428px; top: 800px;
    font-size: 29px; line-height: 42px; color: var(--accent-pink);
    font-weight: 900; letter-spacing: 1px; white-space: nowrap;
  }
</style>
</head>
<body>
<main class="postcard">
  <div class="art art--hand-rose" role="img" aria-label="Vintage illustration of a hand holding a pink rose"></div>
  <div class="art art--portrait" role="img" aria-label="Vintage sepia portrait of a lady in an Edwardian hat"></div>
  <div class="art art--ticket" role="img" aria-label="Faded pink admission ticket stub"></div>
  <div class="art art--boot-bouquet" role="img" aria-label="Vintage turquoise lace-up boot filled with golden roses"></div>
  <div class="art art--scene" role="img" aria-label="Faded sepia vintage scene of ladies in bonnets"></div>

  <h1 class="brand">Lustrea Nail</h1>

  <p class="tagline">Beautiful nails for up to three weeks.<br>No chipping, dulling or fading.<br>Fully mobile with flexible appointments.</p>

  <p class="contact">
    Call MOIRA on 07812604731<br>
    or email lustrea_nails@brivomail.com<br>
    can also follow on Chirper@Lustrea_nails.
  </p>

  <svg class="strokes" viewBox="0 0 560 140" aria-hidden="true">
    <path d="M10 40 C120 0 220 30 320 20 S480 10 545 40 L540 62 C460 40 400 50 320 48 S120 40 12 60 Z" fill="var(--stroke-purple)"/>
    <path d="M0 58 C130 40 240 62 340 60 S480 55 550 72 L548 92 C470 78 400 82 330 84 S120 72 4 82 Z" fill="var(--stroke-blue)" opacity="0.9"/>
    <path d="M30 82 C150 70 260 92 360 88 S470 80 530 92 L528 108 C460 98 400 104 340 106 S150 92 34 100 Z" fill="var(--stroke-yellow)"/>
    <path d="M20 96 C150 86 250 112 350 112 S470 106 550 118 L546 134 C470 124 400 130 330 130 S140 112 24 114 Z" fill="var(--stroke-coral)"/>
  </svg>

  <section class="prices">
    <div>Prices:</div>
    <div class="prices__row"><span>Fingernails</span><span>£20</span></div>
    <div class="prices__row"><span>Toenails</span><span>£20</span></div>
    <div class="prices__row"><span>Both</span><span>£35</span></div>
    <div class="prices__row"><span>Gel Removal</span><span>£10</span></div>
  </section>

  <p class="credentials">Qualified with Palm &amp; Polish Academy UK<br>Insured with QERVOL</p>
</main>
</body>
</html>
```